Thai Takeaway Menu Design

I need a menu re-design for a thai takeaway/restaurant in australia.

Please use content from the existing menu
http://www.platterwink.example/u/menu/7302918?p=1

I'd like to emphasise on
1 - free delivery for order over $40
2 - gluten free and vegetatian option available on most meal (however you want to word it - not fuss)

*remove (the banner order online and save $10)

I'm happy to change the whole concept & design. I particularly like rustic, raw look more than moden ones. Does not need to be flowery or anything like current one :)

Industry/Entity Type

Restaurant

```html
<!DOCTYPE html>
<html lang="en">
<head>
<meta charset="utf-8">
<title>Thai Takeaway Menu</title>
<link href="https://fonts.googleapis.com/css2?family=Arimo:ital,wght@0,700;1,400&family=Pinyon+Script&display=swap" rel="stylesheet">
<style>
:root{
  --stage:#2a1d17;
  --frame:#1a0c07;
  --wood:#6e2f12;
  --paper:#e5ddcc;
  --paper-edge:#d6ccb6;
  --item:#b4461b;
  --price:#4b4234;
  --count:#8a7f6c;
  --heading:#5a5044;
  --rule:#b9ae98;
  --fold:rgba(120,100,70,.18);
  --drinks-box:rgba(160,145,120,.22);
  --badge:#f2e21c;
  --badge-ring:#d9c510;
  --badge-text:#4a3f10;
}
*{margin:0;padding:0;box-sizing:border-box}
html,body{width:1200px;height:1131px;overflow:hidden;background:var(--stage)}
.menu{position:absolute;left:80px;top:165px;width:1055px;height:745px;background:var(--wood);font-family:"Arimo",Arial,sans-serif}
.menu-band{position:absolute;left:0;width:100%;height:15px;background:var(--frame)}
.menu-band.top{top:0}.menu-band.bottom{bottom:0;height:17px}
.paper{position:absolute;left:0;top:0}
.fold{position:absolute;top:40px;width:1px;height:650px;background:var(--fold)}
.photo{position:absolute}
.section{position:absolute}
.section h2{font-family:"Pinyon Script",cursive;font-weight:400;font-size:23px;line-height:22px;height:22px;color:var(--heading);margin-left:-6px}
.items{list-style:none}
.items li{display:flex;justify-content:space-between;align-items:center;height:16.3px;font-size:11px;font-weight:700;color:var(--item);border-bottom:1px dotted var(--rule)}
.items .price{color:var(--price)}
.items .count{color:var(--count);font-weight:400}
.items li.tall{height:27.5px;align-items:flex-end;line-height:11.5px;padding-bottom:2px}
.items em{color:var(--count);font-weight:400}
.delivery{position:absolute;left:388px;top:558px;width:274px;font-size:11px;font-weight:700;color:var(--price)}
.drinks-box{position:absolute;left:730px;top:458px;width:296px;height:180px;border-radius:16px;background:var(--drinks-box)}
.badge{position:absolute;left:320px;top:578px;width:170px;height:152px}
.badge-text{position:absolute;left:340px;top:610px;width:130px;transform:rotate(-14deg);text-align:center;font-size:11.5px;font-weight:700;line-height:13px;color:var(--badge-text)}
</style>
</head>
<body>
<div class="menu">
  <div class="menu-band top"></div>
  <svg class="paper" width="1055" height="745" viewBox="0 0 1055 745">
    <path d="M0 62 L180 58 L300 64 L380 44 L470 36 L560 44 L700 30 L900 46 L1005 52 L1055 78 L1055 680 L900 690 L740 676 L560 684 L340 676 L160 690 L0 682 Z" fill="var(--paper)" stroke="var(--paper-edge)" stroke-width="2"/>
  </svg>
  <div class="fold" style="left:350px"></div>
  <div class="fold" style="left:693px"></div>

  <svg class="photo" style="left:0;top:15px" width="1055" height="230" viewBox="0 0 1055 230" role="img" aria-label="Spice bowls, basil leaves, lime half and frangipani flowers along the top edge">
    <rect x="0" y="10" width="40" height="170" rx="20" fill="#5d8a2c"/>
    <ellipse cx="85" cy="20" rx="75" ry="45" fill="#6a5640"/>
    <ellipse cx="295" cy="20" rx="95" ry="60" fill="#4e6a24"/>
    <ellipse cx="752" cy="30" rx="68" ry="50" fill="#c9c83a"/>
    <ellipse cx="930" cy="20" rx="95" ry="50" fill="#d8c9a0"/>
    <ellipse cx="1040" cy="70" rx="40" ry="55" fill="#2b2118"/>
  </svg>
  <svg class="photo" style="left:0;top:520px" width="1055" height="210" viewBox="0 0 1055 210" role="img" aria-label="Cloves, black pepper, ground spices, dried red chillies, a plate of fish with coriander, cinnamon sticks and spice bowls along the bottom edge">
    <circle cx="8" cy="92" r="32" fill="#4a3524"/>
    <ellipse cx="80" cy="140" rx="65" ry="40" fill="#6a3a2a"/>
    <circle cx="20" cy="178" r="32" fill="#c99a52"/>
    <circle cx="118" cy="180" r="40" fill="#3a3028"/>
    <path d="M195 95 L345 210 L195 210 Z" fill="#a52018"/>
    <ellipse cx="600" cy="170" rx="145" ry="110" fill="#e8ebe4"/>
    <rect x="1020" y="0" width="35" height="115" fill="#8e4a22"/>
    <ellipse cx="920" cy="175" rx="65" ry="50" fill="#7b8a3a"/>
    <ellipse cx="1030" cy="175" rx="45" ry="50" fill="#c2541e"/>
  </svg>

  <svg class="badge" viewBox="0 0 170 152" role="presentation">
    <circle cx="85" cy="76" r="74" fill="var(--badge-ring)"/>
    <circle cx="85" cy="76" r="64" fill="var(--badge)"/>
  </svg>
  <p class="badge-text">All meals<br>can be made to<br>suit your dietary<br>requirements,<br>Gluten Free, Dairy<br>Free, Vegetarian</p>

  <section class="section" style="left:47px;top:87px;width:273px">
    <h2>Entrée</h2>
    <ul class="items">
      <li><span>Spring Rolls* <span class="count">(4)</span></span><span class="price">$6.50</span></li>
      <li><span>Satay Chicken Skewers <span class="count">(4)</span></span><span class="price">$6.50</span></li>
      <li><span>Fish Cakes <span class="count">(4)</span></span><span class="price">$6.50</span></li>
      <li><span>Curry Puffs <span class="count">(4)</span></span><span class="price">$6.50</span></li>
      <li><span>Dim Sim <span class="count">(4)</span></span><span class="price">$6.50</span></li>
      <li><span>Duck Rice Paper Rolls <span class="count">(2)</span></span><span class="price">$6.50</span></li>
      <li><span>Papaya Salad</span><span class="price">$6.50</span></li>
      <li><span>Tofu/w Peanut Sauce*</span><span class="price">$6.50</span></li>
    </ul>
  </section>
  <section class="section" style="left:44px;top:254px;width:273px">
    <h2>Soup</h2>
    <ul class="items">
      <li><span>Tom Yum Prawn*</span><span class="price">$7.50</span></li>
      <li><span>Tom Kha Chicken*</span><span class="price">$7.50</span></li>
    </ul>
  </section>
  <section class="section" style="left:44px;top:316px;width:272px">
    <h2>Curry</h2>
    <ul class="items">
      <li><span>Green Curry Chicken*</span><span class="price">$14.00</span></li>
      <li><span>Panang Chicken*</span><span class="price">$14.00</span></li>
      <li><span>Red Curry Beef*</span><span class="price">$14.00</span></li>
      <li><span>Massaman Beef Curry</span><span class="price">$14.00</span></li>
      <li><span>Red Duck Curry</span><span class="price">$16.90</span></li>
      <li><span>Yellow Curry Chicken*</span><span class="price">$14.00</span></li>
      <li><span>Yellow Curry Prawn</span><span class="price">$16.90</span></li>
    </ul>
  </section>
  <section class="section" style="left:44px;top:465px;width:272px">
    <h2>Vegetable</h2>
    <ul class="items">
      <li><span>Mixed Vegetables*</span><span class="price">$12.50</span></li>
      <li><span>Steamed Veg/w Peanut Sauce*</span><span class="price">$12.50</span></li>
    </ul>
  </section>
  <section class="section" style="left:45px;top:526px;width:271px">
    <h2>Beef</h2>
    <ul class="items">
      <li><span>Grilled Thai Beef Salad</span><span class="price">$14.00</span></li>
      <li><span>Beef w/ Oyster Sauce</span><span class="price">$14.00</span></li>
      <li><span>Beef w/ Vegetable &amp; Peanut Sauce</span><span class="price">$14.00</span></li>
    </ul>
  </section>

  <section class="section" style="left:391px;top:84px;width:273px">
    <h2>Chicken</h2>
    <ul class="items">
      <li><span>Laab Chicken*</span><span class="price">$14.00</span></li>
      <li><span>Chicken/w Sweet Basil*</span><span class="price">$14.00</span></li>
      <li><span>Chicken/w Cashew Nuts*</span><span class="price">$14.00</span></li>
      <li><span>Grilled Chicken/w Salad</span><span class="price">$14.00</span></li>
      <li><span>Southern Style Fried Chicken</span><span class="price">$14.00</span></li>
      <li><span>Crispy Chicken /w Sticky Garlic Sauce</span><span class="price">$14.00</span></li>
    </ul>
  </section>
  <section class="section" style="left:388px;top:216px;width:274px">
    <h2>Pork</h2>
    <ul class="items">
      <li><span>Crispy Pork w/ Asian Greens</span><span class="price">$14.00</span></li>
      <li><span>Sweet &amp; Sour Pork</span><span class="price">$14.00</span></li>
      <li><span>Pork w/ Garlic &amp; Vegetables</span><span class="price">$14.00</span></li>
    </ul>
  </section>
  <section class="section" style="left:389px;top:298px;width:273px">
    <h2>Duck</h2>
    <ul class="items">
      <li><span>Roast Duck /w Vegetable &amp; Hoisin Sauce</span><span class="price">$18.00</span></li>
      <li><span>Duck/w Sweet Basil</span><span class="price">$18.00</span></li>
      <li><span>Honey Glazed Duck/w Vegetable</span><span class="price">$18.00</span></li>
    </ul>
  </section>
  <section class="section" style="left:388px;top:383px;width:274px">
    <h2>Seafood</h2>
    <ul class="items">
      <li><span>Garlic Prawn</span><span class="price">$18.00</span></li>
      <li><span>Tamarind Prawn</span><span class="price">$18.00</span></li>
      <li><span>Laab Fish</span><span class="price">$18.00</span></li>
      <li><span>Crispy Fish/w Sweet Chilli Salsa</span><span class="price">$18.00</span></li>
      <li><span>Chilli &amp; Lime Calamari Salad</span><span class="price">$18.00</span></li>
      <li><span>Salt &amp; Pepper Calamari</span><span class="price">$18.00</span></li>
      <li><span>Spicy Seafood</span><span class="price">$18.00</span></li>
      <li><span>Fish of the Day w/ Shiitake, Ginger &amp; Veg</span><span class="price">$18.00</span></li>
      <li><span>Chu Chee Salmon Curry</span><span class="price">$22.90</span></li>
    </ul>
  </section>
  <p class="delivery">Free delivery for orders over $40</p>

  <section class="section" style="left:737px;top:104px;width:273px">
    <h2>Noodle</h2>
    <ul class="items">
      <li><span>Pad Thai*</span><span class="price">$14.00</span></li>
      <li><span>Pad Thai Prawn</span><span class="price">$18.00</span></li>
      <li><span>Drunken Noodle*</span><span class="price">$14.00</span></li>
      <li><span>Pad See Eew*</span><span class="price">$14.00</span></li>
      <li><span>Seafood Laksa</span><span class="price">$18.00</span></li>
    </ul>
  </section>
  <section class="section" style="left:738px;top:219px;width:272px">
    <h2>Rice</h2>
    <ul class="items">
      <li><span>Rice (S)</span><span class="price">$2.50</span></li>
      <li><span>Rice (L)</span><span class="price">$3.50</span></li>
      <li><span>Coconut Rice (S)</span><span class="price">$4.50</span></li>
      <li><span>Coconut Rice (L)</span><span class="price">$5.50</span></li>
      <li><span>Chicken Fried Rice</span><span class="price">$14.00</span></li>
      <li><span>Roti Bread/w Peanut Sauce</span><span class="price">$5.50</span></li>
    </ul>
  </section>
  <section class="section" style="left:735px;top:354px;width:275px">
    <h2>Dessert</h2>
    <ul class="items">
      <li><span>Black Sticky Rice/w Coconut Cream</span><span class="price">$5.00</span></li>
      <li><span>Tapioca Pudding/w Lychee</span><span class="price">$5.00</span></li>
      <li><span>Toasted Coconut Icecream</span><span class="price">$5.00</span></li>
      <li><span>Mango Icecream</span><span class="price">$5.00</span></li>
    </ul>
  </section>
  <div class="drinks-box"></div>
  <section class="section" style="left:735px;top:464px;width:273px">
    <h2>Drinks</h2>
    <ul class="items">
      <li class="tall"><span>Kola, Diet Kola, Kola Zero, Fizzo,<br>Limeo, Zesto - 375ml</span><span class="price">$2.50</span></li>
      <li class="tall"><span>Zesto, Kola, Diet Kola, Kola Zero, Fizzo,<br>Limeo - 1.25L</span><span class="price">$4.50</span></li>
      <li><span>Orange Juice, Apple Juice</span><span class="price">$3.50</span></li>
      <li><span>Ginger Beer</span><span class="price">$3.50</span></li>
      <li><span>Lemon Lime &amp; Bitters</span><span class="price">$3.50</span></li>
      <li><span>Tealeaf Ice Tea <em>(Green Citrus, Lemon, Peach)</em></span><span class="price">$3.50</span></li>
      <li><span>Sal Montefino Sparkling Mineral Water</span><span class="price">$4.50</span></li>
    </ul>
  </section>

  <div class="menu-band bottom"></div>
</div>
</body>
</html>
```